Digital menu Skydiving company

Design Digital menu/pricelist for our company. It can have dynamic components. We are also looking for a Graphic design for all our projects. Our main goals are to look clean/sharp and professional. Information is in psd file

3 packages Amber Plunge, Harbor Voyage, And Thunder Journey. then we have addons and merchandise

Colors
0293ce
34a7d8
ffffff
fbee3f
3377b5
000000
f37122
ec1f27
e34197

Requirements
Must have
• Sorry If I couldn't get my vision across better, Please see really rough design idea attached. one large picture section that rotates through 3 or 4 pictures. then all the information down the bottom and on right (see menu pricelist attached)

```html
<!DOCTYPE html>
<html lang="en">
<head>
<meta charset="utf-8">
<title>Zenith Skydive – Packages and Pricing</title>
<link href="https://fonts.googleapis.com/css2?family=Jost:wght@500;700;800&display=swap" rel="stylesheet">
<style>
  :root{
    --navy:#1e4a9c;
    --blue:#3377b5;
    --sky:#34a7d8;
    --band-top:#2457a8;
    --band-bottom:#9dbde6;
    --white:#ffffff;
    --gold:#f4c132;
    --gold-deep:#e7a91f;
    --gold-frame:#d99a1a;
    --ink:#1b2a55;
    --rule:#b9861a;
    --bg:#eef1f5;
  }
  *{box-sizing:border-box;margin:0;padding:0}
  html,body{width:1200px;height:857px;overflow:hidden;background:var(--bg)}
  body{font-family:"Jost",sans-serif;color:var(--ink)}
  .menu{position:relative;width:1200px;height:857px;background:var(--white);overflow:hidden}

  .header{position:absolute;left:0;top:0;width:100%;height:190px;background:linear-gradient(180deg,#ffffff 0%,#f3f5f8 100%)}
  .brand{position:absolute;left:44px;top:58px;display:flex;align-items:center;gap:12px}
  .brand-dot{width:26px;height:26px;border-radius:50%;background:var(--sky)}
  .brand-name{font-weight:700;font-size:34px;letter-spacing:1px;color:var(--navy);text-transform:uppercase}
  .title{position:absolute;left:450px;top:46px;font-weight:800;font-size:44px;letter-spacing:3px;color:var(--navy);text-transform:uppercase}

  .band{position:absolute;left:0;top:190px;width:100%;height:240px;background:linear-gradient(180deg,var(--band-top) 0%,#4f80c4 55%,var(--band-bottom) 100%)}

  .photo{position:absolute;width:226px;height:210px}
  .photo .corner{position:absolute;width:70px;height:70px;background:var(--gold-frame)}
  .photo .frame{position:absolute;inset:0;border:7px solid var(--white);box-shadow:0 6px 14px rgba(0,0,0,.35)}
  .photo .fill{width:100%;height:100%}
  .photo-1{left:40px;top:200px}
  .photo-1 .corner{left:-16px;top:-16px}
  .photo-2{left:330px;top:160px}
  .photo-2 .corner{right:-16px;bottom:-16px}
  .photo-3{left:610px;top:150px}
  .photo-3 .corner{left:-16px;top:-16px}
  .photo-4{left:900px;top:150px}
  .photo-4 .corner{right:-16px;top:-16px}
  .sky-a{background:linear-gradient(180deg,#6f98c9 0%,#9fb3c8 45%,#8c7e6a 100%)}
  .sky-b{background:linear-gradient(180deg,#2f78c8 0%,#7fb2e2 55%,#c9d6e0 100%)}
  .sky-c{background:linear-gradient(180deg,#8fb4d8 0%,#e7c9a1 60%,#b48a5f 100%)}
  .sky-d{background:linear-gradient(180deg,#3a82cf 0%,#8fbbe4 55%,#a48b70 100%)}

  .pricing{position:absolute;left:0;top:430px;width:100%;height:427px;background:linear-gradient(135deg,var(--gold) 0%,#f7cc45 50%,var(--gold-deep) 100%);display:flex}
  .package{position:relative;padding:26px 22px 20px;border-right:2px solid var(--rule);text-transform:uppercase}
  .package-amber{width:380px}
  .package-harbor{width:255px}
  .package-thunder{width:300px}
  .package h2{font-weight:800;font-size:26px;line-height:1.02;color:var(--navy)}
  .package .tagline{margin-top:14px;font-weight:700;font-size:17px;color:var(--navy);line-height:1.15}
  .items{list-style:none;margin-top:14px;font-weight:500;font-size:15px;line-height:1.3;color:var(--ink)}
  .items li{display:flex;justify-content:space-between;gap:8px}
  .items .price{font-weight:700;color:var(--navy)}
  .total{position:absolute;right:22px;bottom:72px;font-weight:800;font-size:18px;color:var(--navy)}

  .merch{flex:1;padding:20px 18px;display:flex;flex-direction:column;gap:14px}
  .merch-shot{flex:1;border:4px solid var(--white);box-shadow:0 4px 10px rgba(0,0,0,.3)}
  .merch-1{background:linear-gradient(90deg,#b32a2a 0%,#f1e6d8 50%,#c73a3a 100%)}
  .merch-2{background:linear-gradient(90deg,#6f9a3b 0%,#e8d48a 50%,#8bb24a 100%)}
  .merch-3{background:linear-gradient(90deg,#2a5fa8 0%,#e6a845 50%,#b22d2d 100%)}
</style>
</head>
<body>
<main class="menu">
  <header class="header">
    <div class="brand"><span class="brand-dot"></span><span class="brand-name">Zenith Skydive</span></div>
    <h1 class="title">Packages and Pricing</h1>
  </header>

  <div class="band"></div>

  <div class="photo photo-1"><span class="corner"></span><div class="frame"><div class="fill sky-a" role="img" aria-label="Aerial view over a canyon from the aircraft"></div></div></div>
  <div class="photo photo-2"><span class="corner"></span><div class="frame"><div class="fill sky-b" role="img" aria-label="Tandem skydivers in freefall above the landscape"></div></div></div>
  <div class="photo photo-3"><span class="corner"></span><div class="frame"><div class="fill sky-c" role="img" aria-label="Parachute canopy over the desert at sunset"></div></div></div>
  <div class="photo photo-4"><span class="corner"></span><div class="frame"><div class="fill sky-d" role="img" aria-label="Tandem pair in freefall with the ground far below"></div></div></div>

  <section class="pricing">
    <article class="package package-amber">
      <h2>Amber Plunge<br>16,000ft</h2>
      <p class="tagline">The skydive is naked,<br>not you...</p>
      <ul class="items">
        <li><span>Tandem skydive from 16,000ft AGL</span><span class="price">$329</span></li>
        <li><span>Certificate of achievement</span><span class="price"></span></li>
        <li><span>T-Shirt Short Sleeve</span><span class="price">$25</span></li>
        <li><span>T-Shirt Long Sleeve</span><span class="price">$30</span></li>
        <li><span>Sweat Shirts</span><span class="price">$35</span></li>
        <li><span>Hoodies</span><span class="price">$45</span></li>
        <li><span>Goggles from</span><span class="price">$12</span></li>
      </ul>
    </article>

    <article class="package package-harbor">
      <h2>Harbor Voyage<br>16,000ft</h2>
      <p class="tagline">Skydive &amp; share<br>the memories...</p>
      <ul class="items">
        <li><span>Tandem skydive from 16,000ft AGL</span></li>
        <li><span>Photos</span></li>
        <li><span>Videos</span></li>
        <li><span>Certificate of achievement</span></li>
      </ul>
      <span class="total">$459</span>
    </article>

    <article class="package package-thunder">
      <h2>Thunder Journey<br>16,000ft</h2>
      <p class="tagline">For the thrill seeker...</p>
      <ul class="items">
        <li><span>Tandem skydive from 16,000ft AGL</span><span class="price">$319</span></li>
        <li><span>Photos</span><span class="price">$99</span></li>
        <li><span>Videos</span><span class="price">$99</span></li>
        <li><span>Extreme extras</span><span class="price">$50</span></li>
        <li><span>Freefall camera skydive</span><span class="price"></span></li>
        <li><span>T-Shirt</span><span class="price"></span></li>
        <li><span>Certificate of achievement</span><span class="price"></span></li>
      </ul>
      <span class="total">$499</span>
    </article>

    <aside class="merch">
      <div class="merch-shot merch-1" role="img" aria-label="Shop shelf with red branded merchandise"></div>
      <div class="merch-shot merch-2" role="img" aria-label="Display of apparel and accessories"></div>
      <div class="merch-shot merch-3" role="img" aria-label="Counter with souvenirs and gear"></div>
    </aside>
  </section>
</main>
</body>
</html>
```